High Quality Business card for Property Management Agency - Super Classy and professional design

High Quality Business card design.

We need a business card designed for our Property Management Agency.
We are located on Sydney's Northern Beaches and manage beautiful properties along the beach and harbor.
We need a design that oozes modern, classy and professional.
I would like it to be double sided with contact details and logo on the front and just the logo on the back.

I need a print ready PDF version of the file as well as an editable photoshop (PSD) version of the file.

Logo and information details attached.

Target Market(s)

Property owners/investors, Male and Female Aged 28-65

Industry/Entity Type

Real Estate

Contact Information for Business Card

Tom Carrick
Tel: 0467 239 018
Email: tom@harvestlaneestates.com.au
Website: www.harvestlaneestates.com.au
Address: Level 2, 17 Wattlecourt Rd, Dunmarra NSW 2187

Font styles to use
Sans Serif

Requirements
Must have
• - Logo front and back
• - Business card details listed above and attached
• - Colour
Nice to have
• Sleek and professional

```html
<!DOCTYPE html>
<html lang="en">
<head>
<meta charset="utf-8">
<title>Harvest Lane Estates – Business Card</title>
<link rel="stylesheet" href="https://fonts.googleapis.com/css2?family=Montserrat:wght@400;500;600;700&display=swap">
<style>
  :root {
    --backdrop: #e4e6e8;
    --paper: #ffffff;
    --ink: #1a1c1d;
    --teal: #137c8c;
    --teal-bright: #2aa3a8;
    --card-dark: #111717;
    --white: #ffffff;
  }
  * { margin: 0; padding: 0; box-sizing: border-box; }
  html, body {
    width: 1200px;
    height: 927px;
    overflow: hidden;
    background: var(--backdrop);
    font-family: "Montserrat", sans-serif;
  }
  .canvas { position: relative; width: 1200px; height: 927px; }
  .card {
    position: absolute;
    top: 84px;
    width: 433px;
    height: 758px;
  }
  .card--front { left: 148px; background: var(--paper); color: var(--ink); }
  .card--back { left: 619px; background: var(--card-dark); color: var(--white); }

  .brand {
    position: absolute;
    left: 0; right: 0;
    display: flex;
    align-items: center;
    justify-content: center;
    gap: 10px;
    font-weight: 700;
    letter-spacing: 0.5px;
  }
  .brand__dot { border-radius: 50%; background: var(--teal-bright); flex: none; }
  .card--front .brand { top: 138px; font-size: 27px; color: var(--ink); }
  .card--front .brand__dot { width: 22px; height: 22px; }
  .card--back .brand { top: 362px; font-size: 27px; color: var(--teal-bright); }
  .card--back .brand__dot { width: 26px; height: 26px; }

  .rule {
    position: absolute;
    left: 73px;
    width: 287px;
    height: 2px;
    background: linear-gradient(90deg, transparent, var(--ink) 15%, var(--ink) 85%, transparent);
  }
  .rule--top { top: 452px; }
  .rule--bottom { top: 696px; }

  .details {
    position: absolute;
    top: 466px;
    left: 0; right: 0;
    text-align: center;
    font-size: 19px;
    line-height: 27px;
  }
  .details__name {
    font-size: 35px;
    line-height: 40px;
    font-weight: 700;
    color: var(--teal);
    letter-spacing: 1px;
    margin-bottom: 12px;
  }
  .details__icons {
    display: flex;
    justify-content: center;
    gap: 8px;
    margin: 10px 0 6px;
    height: 16px;
  }
  .details__icons svg { width: 16px; height: 16px; }
  .web__domain { color: var(--teal); font-weight: 600; }

  .card--back .web {
    position: absolute;
    top: 662px;
    left: 0; right: 0;
    text-align: center;
    font-size: 19px;
    letter-spacing: 0.3px;
  }
  .card--back .web__domain { color: var(--white); }
</style>
</head>
<body>
<main class="canvas">
  <section class="card card--front">
    <div class="brand"><span class="brand__dot"></span><span>HARVEST LANE ESTATES</span></div>

    <div class="rule rule--top"></div>
    <div class="details">
      <h1 class="details__name">TOM CARRICK</h1>
      <p>Level 2, 17 Wattlecourt Rd</p>
      <p>Dunmarra NSW 2187</p>
      <div class="details__icons">
        <svg viewBox="0 0 16 16" aria-hidden="true"><path d="M4 1.5 L6 4.5 L4.8 6 Q6.5 9.5 10 11.2 L11.5 10 L14.5 12 L13 14.5 Q6 13.5 1.8 4 Z" fill="none" stroke="var(--teal)" stroke-width="1.4" stroke-linejoin="round"/></svg>
        <svg viewBox="0 0 16 16" aria-hidden="true"><rect x="1.5" y="3.5" width="13" height="9" fill="none" stroke="var(--teal)" stroke-width="1.4"/><path d="M1.5 3.5 L8 9 L14.5 3.5" fill="none" stroke="var(--teal)" stroke-width="1.4"/></svg>
        <svg viewBox="0 0 16 16" aria-hidden="true"><g fill="none" stroke="var(--teal)" stroke-width="1.2"><circle cx="8" cy="8" r="6.5"/><ellipse cx="8" cy="8" rx="3" ry="6.5"/><path d="M1.5 8 H14.5 M2.5 4.8 H13.5 M2.5 11.2 H13.5"/></g></svg>
      </div>
      <p>0467 239 018</p>
      <p>tom@harvestlaneestates.com.au</p>
      <p class="web">www.<span class="web__domain">harvestlaneestates</span>.com.au</p>
    </div>
    <div class="rule rule--bottom"></div>
  </section>

  <section class="card card--back">
    <div class="brand"><span class="brand__dot"></span><span>HARVEST LANE ESTATES</span></div>
    <p class="web">www.<span class="web__domain">harvestlaneestates</span>.com.au</p>
  </section>
</main>
</body>
</html>
```